New Software Development Firm Needs Stationery

Brindle Works, LLC is a new software development firm specializing in document management and custom engineering applications. We just completed a logo design project on PixelHarbor.

We also have an open project right now on PixelHarbor for business card design. ** We highly encourage you to submit designs to both projects as we want the two designs to have the same look and feel.

Design must be provided for coordinated letterhead and envelopes that works with the selected business card design on the other project.

We want a clean, professional and modern look that works well with our logo. We also require a recommendation for what PC font to use when printing on the new letterhead and envelopes.

The final submission must include source Photoshop or Illustrator files and any fonts used must be specified exactly.

Target Market(s)

Small to medium business professionals - including manufacturers, civil engineering firms, government agencies, architects, as well as general business.

Industry/Entity Type

Software

Requirements
Must have
• Must work very well with logo and business card design. Must work well with a specified and readily-available font on most PCs.
Nice to have
• White letterhead and envelopes are probably preferred, but we're open to suggestions!

```html
<!DOCTYPE html>
<html lang="en">
<head>
<meta charset="utf-8">
<title>Brindle Works, LLC – Stationery</title>
<link rel="stylesheet" href="https://fonts.googleapis.com/css2?family=Exo+2:wght@500&family=Arimo:wght@400&display=swap">
<style>
  :root {
    --ink: #0b0b0b;
    --paper: #ffffff;
    --card-grey: #eeeeec;
    --stage: #2b2b2b;
    --text-grey: #6d6d6d;
    --text-dark: #1c1c1c;
    --accent: #e0262b;
    --watermark: #d9d9d9;
    --rule: #bdbdbd;
  }
  * { box-sizing: border-box; margin: 0; padding: 0; }
  html, body { width: 1200px; height: 927px; overflow: hidden; }
  body {
    background: var(--stage);
    font-family: "Arimo", Arial, sans-serif;
    position: relative;
  }
  .wordmark { font-family: "Exo 2", sans-serif; font-weight: 500; letter-spacing: 0.5px; white-space: nowrap; }

  /* Letterhead */
  .letterhead {
    position: absolute; left: 600px; top: 70px; width: 560px; height: 790px;
    background: var(--paper);
  }
  .letterhead__band {
    position: absolute; left: 0; top: 20px; width: 100%; height: 46px;
    background: linear-gradient(90deg, var(--ink) 0%, #222 70%, var(--ink) 100%);
  }
  .letterhead__band .wordmark {
    position: absolute; left: 16px; top: 7px; color: var(--paper); font-size: 24px;
  }
  .letterhead__band .band-rule {
    position: absolute; left: 190px; right: 10px; top: 32px; height: 1px; background: #9a9a9a;
  }
  .contact { color: var(--text-grey); font-size: 8.5px; line-height: 1.2; }
  .contact .phones { margin-top: 4px; font-size: 6.5px; line-height: 1.4; }
  .contact .phones b { color: var(--accent); font-weight: 400; margin-right: 4px; }
  .letterhead .contact { position: absolute; left: 18px; top: 70px; }
  .letterhead__watermark {
    position: absolute; left: 0; right: 0; top: 380px; text-align: center;
    color: var(--watermark); font-size: 54px;
  }
  .letterhead__footer-rule {
    position: absolute; left: 0; right: 0; bottom: 30px; height: 1px; background: var(--rule);
  }
  .letterhead__footer {
    position: absolute; left: 0; right: 0; bottom: 6px; height: 20px;
    background: var(--ink); color: var(--paper); text-align: center;
    font-size: 10px; line-height: 20px;
  }

  /* Business cards */
  .card {
    position: absolute; width: 260px; height: 150px; border-radius: 9px; overflow: hidden;
  }
  .card--front {
    left: 40px; top: 110px;
    background: radial-gradient(ellipse at 40% 40%, #2a2a2a 0%, var(--ink) 70%);
  }
  .card--front .wordmark {
    position: absolute; left: 0; right: 0; top: 50px; text-align: center;
    color: var(--paper); font-size: 28px;
  }
  .card--front .card__web {
    position: absolute; left: 0; right: 0; bottom: 12px; text-align: center;
    color: var(--paper); font-size: 8px;
  }
  .card--back { left: 320px; top: 110px; background: var(--card-grey); }
  .card--back .wordmark { position: absolute; left: 12px; top: 10px; color: var(--text-dark); font-size: 16px; }
  .card--back .contact { position: absolute; left: 12px; top: 32px; color: var(--text-dark); font-size: 6px; }
  .card--back .contact .phones { font-size: 5px; }
  .card__person { position: absolute; left: 140px; top: 74px; color: var(--text-dark); font-size: 6px; line-height: 1.35; }
  .card__name { color: var(--accent); font-size: 9px; }
  .card__role { font-size: 7.5px; margin-bottom: 4px; }
  .card__lines { margin-bottom: 4px; }

  /* Envelope */
  .envelope {
    position: absolute; left: 40px; top: 480px; width: 520px; height: 300px;
    background: var(--paper);
  }
  .envelope__flap {
    position: absolute; left: 0; top: 0; width: 100%; height: 52px;
    background: var(--ink); border-radius: 0 0 0 0;
  }
  .envelope__flap .wordmark {
    position: absolute; left: 0; right: 0; top: 12px; text-align: center;
    color: var(--paper); font-size: 20px; transform: rotate(180deg);
  }
  .envelope .wordmark--sender { position: absolute; left: 18px; top: 68px; color: var(--text-dark); font-size: 26px; }
  .envelope .contact { position: absolute; left: 20px; top: 104px; color: var(--text-dark); }
  .envelope__window {
    position: absolute; left: 300px; top: 168px; width: 190px; height: 90px;
    border: 1px solid #9c9c9c; border-radius: 10px;
  }
  .envelope__web { position: absolute; left: 360px; top: 270px; font-size: 9px; color: var(--text-dark); }
</style>
</head>
<body>

  <section class="letterhead" aria-label="Letterhead">
    <div class="letterhead__band">
      <span class="wordmark">Brindle Works</span>
      <span class="band-rule"></span>
    </div>
    <div class="contact">
      1420 Harbor Lane<br>Fairview, OR<br>97024
      <div class="phones"><b>T :</b>- 55 3 4120 7781<br><b>F :</b>- 55 318 642 905</div>
    </div>
    <div class="letterhead__watermark wordmark">Brindle Works</div>
    <div class="letterhead__footer-rule"></div>
    <div class="letterhead__footer">www.brindleworks.com</div>
  </section>

  <section class="card card--front" aria-label="Business card front">
    <div class="wordmark">Brindle Works</div>
    <div class="card__web">www.brindleworks.com</div>
  </section>

  <section class="card card--back" aria-label="Business card back">
    <div class="wordmark">Brindle Works</div>
    <div class="contact">
      1420 Harbor Lane<br>Fairview, OR<br>97024
      <div class="phones"><b>T :</b>- 55 3 4120 7781<br><b>F :</b>- 55 318 642 905</div>
    </div>
    <div class="card__person">
      <div class="card__name">Full Name</div>
      <div class="card__role">Operation Manager</div>
      <div class="card__lines">T :&nbsp; - 55 3 4120 7781<br>M :&nbsp; - 55 318 642 905</div>
      <div>E :&nbsp; name@brindleworks.com<br>W :&nbsp; www.brindleworks.com</div>
    </div>
  </section>

  <section class="envelope" aria-label="Envelope">
    <div class="envelope__flap"><div class="wordmark">Brindle Works</div></div>
    <div class="wordmark wordmark--sender">Brindle Works</div>
    <div class="contact">
      1420 Harbor Lane<br>Fairview, OR<br>97024
      <div class="phones"><b>T :</b>- 55 3 4120 7781<br><b>F :</b>- 55 318 642 905</div>
    </div>
    <div class="envelope__window"></div>
    <div class="envelope__web">www.brindleworks.com</div>
  </section>

</body>
</html>
```